BrewHaunt coffee packaging design

We need a vector design (AI) for the printing of our coffee bags.

The bags are double sided. Front will be simple with logo and web address. Back will have lots of information (below) and the wording can be changed to suit if required.

Actual bag dimensions are: 240mm wide x 335mm high (each side) artwork should be inside those sizes.

Front:
Requires - BrewHaunt cup logo, web address (brewhaunt.com.au) in lowercase Papyrus font and the words BREW HAUNT in uppercase.
**added** The front will also need a 90mm x 35mm no artwork area so we can place a sticker.

Back:
1.
Velvet Kettle Logo (needs to be entire unmodified logo) and the tagline of "Overall winner of Australia's biggest coffee roasting competition"

2.
BrewHaunt is a family business, proudly Australian owned and operated. We strive to provide amazing coffee, excellent service and great value to all our customers.

3.
Our coffee is fresh roasted to order and shipped same day.

4.
50c from every kilogram sold goes directly to projects in coffee growing regions. TrueLoop is the Fairest Trade of all - see: trueloop.net

Logos are attached and higher resolution ones are available if needed.

Requirements
Must have
• Per the description, BrewHaunt logo and webaddress on the front and Velvet Kettle logo on the back are required.

```html
<!DOCTYPE html>
<html lang="en">
<head>
<meta charset="utf-8">
<title>BrewHaunt coffee bag – front and back</title>
<link href="https://fonts.googleapis.com/css2?family=Macondo&family=Arimo:ital,wght@0,400;0,700;1,700&display=swap" rel="stylesheet">
<style>
  :root{
    --backdrop:#f8f1b8;
    --maroon:#7b2a32;
    --maroon-dark:#5e1d24;
    --brown:#5a2a1c;
    --brown-soft:#8a5a44;
    --tan:#b08a5e;
    --cream:#ede3d2;
    --sand:#d9c6a8;
    --grey:#cfcac4;
    --white:#ffffff;
  }
  *{box-sizing:border-box;margin:0;padding:0}
  html,body{width:1200px;height:1168px;overflow:hidden;background:var(--backdrop)}
  .canvas{position:relative;width:1200px;height:1168px}

  .bag-side{position:absolute;width:400px;height:596px;background:var(--maroon);overflow:hidden}
  .bag-side--front{left:140px;top:286px}
  .bag-side--back{left:660px;top:286px}

  /* FRONT */
  .front-frame{position:absolute;left:22px;top:26px;width:356px;height:548px;border:3px solid var(--tan);border-radius:14px}
  .brand-title{position:absolute;left:0;right:0;top:40px;text-align:center;font-family:"Macondo",cursive;font-weight:400;color:var(--cream);font-size:78px;line-height:70px;letter-spacing:2px}
  .cup-field{position:absolute;left:12px;top:236px;width:376px;height:290px;
    background:
      radial-gradient(ellipse 62% 50% at 50% 52%,rgba(138,90,68,.35),rgba(138,90,68,0) 70%),
      linear-gradient(160deg,var(--cream),var(--grey) 55%,var(--cream));}
  .cup-brand{position:absolute;left:0;right:0;top:236px;height:290px;display:flex;flex-direction:column;align-items:center;justify-content:center;gap:14px;font-family:"Macondo",cursive;font-size:60px;line-height:64px;color:var(--brown)}
  .cup-brand .dot{width:96px;height:96px;border-radius:50%;background:var(--brown)}
  .web-strip{position:absolute;left:12px;right:12px;top:532px;height:50px;background:var(--maroon-dark);border-radius:8px;text-align:center;font-family:"Macondo",cursive;font-size:34px;line-height:50px;color:var(--cream);letter-spacing:1px}

  /* BACK */
  .back-lead{position:absolute;left:0;right:0;top:20px;text-align:center;font-family:"Arimo",sans-serif;font-style:italic;font-weight:700;color:var(--white);font-size:20px;line-height:27px}
  .back-about{position:absolute;left:20px;right:20px;top:80px;text-align:center;font-family:"Arimo",sans-serif;color:var(--white);font-size:10.5px;line-height:13px}
  .back-panel{position:absolute;left:44px;top:128px;width:312px;height:370px;background:linear-gradient(170deg,var(--cream),var(--sand));border:3px solid var(--tan)}
  .award-mark{position:absolute;left:52px;top:140px;display:flex;flex-direction:column;align-items:center;gap:4px;font-family:"Arimo",sans-serif;font-size:10px;font-weight:700;color:var(--brown)}
  .award-mark .dot{width:48px;height:48px;border-radius:50%;background:var(--tan)}
  .award-band{position:absolute;left:-30px;top:206px;width:460px;height:60px;background:var(--maroon);transform:rotate(-13deg);display:flex;align-items:center;justify-content:center;text-align:center;font-family:"Arimo",sans-serif;color:var(--white);font-size:18px;line-height:21px}
  .loop-name{position:absolute;left:0;right:0;top:276px;text-align:center;font-family:"Macondo",cursive;font-size:36px;color:var(--brown)}
  .loop-visual{position:absolute;left:120px;top:326px;width:160px;height:100px;border-radius:50%;background:radial-gradient(circle at 55% 35%,#b9b9b9,#6a4634 55%,#3a2418)}
  .loop-tagline{position:absolute;left:60px;right:60px;top:436px;display:flex;align-items:center;gap:10px;font-family:"Macondo",cursive;font-size:15px;color:var(--brown)}
  .loop-tagline .rule{flex:1;border-top:2px solid var(--brown);border-bottom:2px solid var(--brown);height:6px}
  .back-footer{position:absolute;left:14px;right:14px;top:510px;text-align:center;font-family:"Arimo",sans-serif;font-style:italic;font-weight:700;color:var(--white);font-size:12.5px;line-height:16px}
</style>
</head>
<body>
<main class="canvas">
  <section class="bag-side bag-side--front" aria-label="Bag front">
    <div class="front-frame"></div>
    <h1 class="brand-title">BREW<br>HAUNT</h1>
    <div class="cup-field" role="img" aria-label="Brown steaming cup mark on a light paint-splatter texture"></div>
    <div class="cup-brand"><span class="dot"></span>BrewHaunt</div>
    <div class="web-strip">brewhaunt.com.au</div>
  </section>

  <section class="bag-side bag-side--back" aria-label="Bag back">
    <p class="back-lead">Our coffee is fresh roasted<br>to order and shipped same day.</p>
    <p class="back-about">BrewHaunt is a family business, proudly Australian owned and operated. We strive to provide amazing coffee, excellent service and great value to all our customers.</p>
    <div class="back-panel" role="img" aria-label="Soft beige splatter texture panel"></div>
    <div class="award-mark"><span class="dot"></span>Velvet Kettle</div>
    <div class="award-band">Overall winner of Australia's<br>biggest coffee roasting competition</div>
    <div class="loop-name">TrueLoop</div>
    <div class="loop-visual" role="img" aria-label="Photo of a coin resting on a roasted coffee bean"></div>
    <div class="loop-tagline"><span class="rule"></span>“giving a little back”<span class="rule"></span></div>
    <p class="back-footer">50c from every kilogram sold goes directly to projects<br>in coffee growing regions. TrueLoop is<br>the Fairest Trade of all - see: trueloop.net</p>
  </section>
</main>
</body>
</html>
```